Certificate of Completion - Educational Trainings

We are looking for a certificate of completion for individuals who complete one of our specific trainings. Files should be provided in a Word (docx) or PowerPoint (pptx) format. The "Talmoray example.png" file is to show necessary information. Copies of logos have been included for design purposes.

Target Market(s)

Training Participants

Industry/Entity Type

Healthcare

Font styles to use
Sans Serif

```html
<!DOCTYPE html>
<html lang="en">
<head>
<meta charset="utf-8">
<title>Talmoray Certificate of Completion</title>
<link rel="stylesheet" href="https://fonts.googleapis.com/css2?family=Montserrat:ital,wght@0,700;1,400;1,500&family=UnifrakturMaguntia&display=swap">
<style>
  :root {
    --green-dark: #14532b;
    --green-mid: #0b6b25;
    --green-light: #7aaa58;
    --gold-dark: #a77c38;
    --gold-mid: #e6cf6a;
    --gold-pale: #ede09a;
    --gold-title: #c4962e;
    --silver: #b7b7b7;
    --ink: #111111;
    --text: #3c3c3c;
    --text-soft: #555555;
    --paper: #ffffff;
  }
  * { margin: 0; padding: 0; box-sizing: border-box; }
  html, body { width: 1200px; height: 927px; overflow: hidden; background: var(--paper); }
  .certificate {
    position: relative;
    width: 1200px;
    height: 927px;
    background: var(--paper);
    font-family: "Montserrat", Arial, sans-serif;
    color: var(--text);
  }
  .bands { position: absolute; inset: 0; }
  .brand {
    position: absolute;
    left: 60px;
    top: 100px;
    display: flex;
    align-items: center;
    gap: 22px;
  }
  .brand-dot {
    width: 78px;
    height: 78px;
    border-radius: 50%;
    background: var(--green-mid);
  }
  .brand-name {
    font-weight: 700;
    font-size: 58px;
    letter-spacing: 7px;
    color: var(--ink);
    line-height: 1;
  }
  .brand-divider {
    position: absolute;
    left: 718px;
    top: 125px;
    width: 2px;
    height: 33px;
    background: var(--text);
  }
  .sponsor-info {
    position: absolute;
    left: 759px;
    top: 122px;
    font-style: italic;
    font-weight: 500;
    font-size: 14.3px;
    letter-spacing: 1.3px;
    line-height: 18px;
    color: var(--text);
    text-transform: uppercase;
  }
  .title {
    position: absolute;
    left: 0;
    right: 0;
    top: 184px;
    text-align: center;
    font-family: "UnifrakturMaguntia", "Times New Roman", serif;
    font-weight: 400;
    font-size: 90px;
    line-height: 1;
    color: var(--gold-title);
    letter-spacing: 1px;
  }
  .awarded-to {
    position: absolute;
    left: 0;
    right: 0;
    top: 291px;
    text-align: center;
    font-style: italic;
    font-weight: 500;
    font-size: 22px;
    letter-spacing: 2.4px;
    color: var(--text);
  }
  .recipient-line {
    position: absolute;
    left: 323px;
    top: 431px;
    width: 553px;
    height: 2px;
    background: var(--text);
  }
  .course-details {
    position: absolute;
    left: 0;
    right: 0;
    top: 454px;
    text-align: center;
    font-style: italic;
    font-size: 20.5px;
    line-height: 25.5px;
    letter-spacing: 0.3px;
    color: var(--text-soft);
  }
  .seal-placeholder {
    position: absolute;
    left: 493px;
    top: 562px;
    width: 212px;
    height: 250px;
    background: linear-gradient(160deg, var(--gold-mid) 0%, var(--gold-dark) 45%, var(--green-dark) 100%);
  }
  .signature-block {
    position: absolute;
    top: 759px;
    width: 224px;
    border-top: 2px solid var(--text);
    text-align: center;
    padding-top: 9px;
    font-style: italic;
    font-weight: 500;
    font-size: 16.5px;
    letter-spacing: 0.4px;
    color: var(--text);
  }
  .signature-block.date { left: 92px; }
  .signature-block.consultant { left: 884px; }
  .credit-note {
    position: absolute;
    left: 36px;
    right: 60px;
    top: 828px;
    font-style: italic;
    font-weight: 500;
    font-size: 13.4px;
    letter-spacing: 0.2px;
    color: var(--text);
    white-space: nowrap;
  }
</style>
</head>
<body>
<main class="certificate">
  <svg class="bands" width="1200" height="927" viewBox="0 0 1200 927" aria-hidden="true">
    <defs>
      <linearGradient id="greenTop" x1="0" x2="1" y1="0" y2="0">
        <stop offset="0" stop-color="#80ac5a"/>
        <stop offset="0.6" stop-color="#0b6b25"/>
        <stop offset="1" stop-color="#1a4d2a"/>
      </linearGradient>
      <linearGradient id="greenBottom" x1="0" x2="1" y1="0" y2="0">
        <stop offset="0" stop-color="#1a4d2a"/>
        <stop offset="0.4" stop-color="#0b6b25"/>
        <stop offset="1" stop-color="#80ac5a"/>
      </linearGradient>
      <linearGradient id="goldBand" x1="0" x2="1" y1="0" y2="0">
        <stop offset="0" stop-color="#a77c38"/>
        <stop offset="0.35" stop-color="#e6cf6a"/>
        <stop offset="0.5" stop-color="#ede09a"/>
        <stop offset="0.7" stop-color="#e6cf6a"/>
        <stop offset="1" stop-color="#a77c38"/>
      </linearGradient>
      <linearGradient id="silverBand" x1="0" x2="1" y1="0" y2="0">
        <stop offset="0" stop-color="#a9a9a9"/>
        <stop offset="1" stop-color="#d2d2d2"/>
      </linearGradient>
    </defs>
    <polygon points="168,0 1200,0 1200,36 199,36" fill="url(#greenTop)"/>
    <polygon points="444,36 650,36 664,55 464,55" fill="url(#silverBand)"/>
    <polygon points="626,36 1200,36 1200,76 654,76" fill="url(#goldBand)"/>
    <polygon points="0,851 547,851 574,891 0,891" fill="url(#goldBand)"/>
    <polygon points="560,871 736,871 755,891 574,891" fill="url(#silverBand)"/>
    <polygon points="0,891 1000,891 1032,927 0,927" fill="url(#greenBottom)"/>
  </svg>

  <header>
    <div class="brand">
      <span class="brand-dot"></span>
      <span class="brand-name">TALMORAY</span>
    </div>
    <span class="brand-divider"></span>
    <p class="sponsor-info">48 Harbor Road, Ste. 310 Bayfield, ME 04920<br>Central Registry Sponsor Number 70218</p>
  </header>

  <h1 class="title">Certificate of Completion</h1>
  <p class="awarded-to">THIS CERTIFICATE IS AWARDED TO</p>
  <div class="recipient-line"></div>

  <p class="course-details">For successful completion of Best Practices:<br>Budget Process/Budget Building Completed Online Field of Study Finance<br>CPE Credits: 1</p>

  <div class="seal-placeholder" role="img" aria-label="Gold and green achievement award seal with ribbons"></div>

  <div class="signature-block date">COMPLETION DATE</div>
  <div class="signature-block consultant">SENIOR CONSULTANT</div>

  <p class="credit-note">IN ACCORDANCE WITH THE STANDARD OF THE CENTRAL REGISTRY OF CPE SPONSORS, CPE CREDITS HAVE BEEN GRANTED BASED ON A 50 MINUTE HOUR.</p>
</main>
</body>
</html>
```